BrightGable.net
Professional
Hal Pemberly
President
718 Quillmoor Rd.
Longwood, FL 32814
hpemberly@brightgable.net
www.brightgable.net
The logo file actually has 2 versions of our logo on it. One with the symbol on the left side of the name and one with the symbol above the name. I did this so that when you are designing the business card you can pick which ever one works best with your design. I also have ones with various other changes (i.e. without the lines) if anyone needs them.

```html
<!DOCTYPE html>
<html lang="en">
<head>
<meta charset="utf-8">
<title>BrightGable.net Stationery</title>
<link rel="stylesheet" href="https://fonts.googleapis.com/css2?family=Arimo:wght@400;700&display=swap">
<style>
  :root {
    --page: #ffffff;
    --frame: #e2e4e6;
    --paper: #ffffff;
    --shadow: rgba(0, 0, 0, 0.28);
    --ink: #4a4f55;
    --ink-soft: #8a9097;
    --brand: #2c5f92;
    --brand-deep: #0f2f56;
    --brand-mid: #2f6fa8;
    --brand-light: #7fb2dc;
    --faint: #eef1f4;
  }
  * { box-sizing: border-box; margin: 0; padding: 0; }
  html, body { width: 1200px; height: 681px; overflow: hidden; background: var(--page); }
  body { font-family: "Arimo", Arial, sans-serif; color: var(--ink); position: relative; }
  address { font-style: normal; }

  .showcase {
    position: absolute; left: 19px; top: 19px; width: 1162px; height: 629px;
    border: 2px solid var(--frame); background: var(--page);
  }
  .piece {
    position: absolute; background: var(--paper); overflow: hidden;
    box-shadow: 2px 3px 6px var(--shadow);
  }
  .corner-band { position: absolute; left: 0; top: 0; }

  .brand-lockup { position: absolute; display: flex; flex-direction: column; gap: 2px; }
  .brand-tag { font-size: 6px; color: var(--ink-soft); letter-spacing: 0.3px; white-space: nowrap; }
  .brand-name { font-weight: 700; color: var(--brand); line-height: 1; white-space: nowrap; }
  .brand-dot { display: inline-block; border-radius: 50%; background: var(--brand); vertical-align: middle; margin-right: 5px; }

  /* envelope front */
  .envelope-front { left: 55px; top: 103px; width: 502px; height: 204px; }
  .envelope-front .brand-lockup { left: 46px; top: 12px; }
  .envelope-front .brand-name { font-size: 18px; }
  .envelope-front .brand-dot { width: 13px; height: 13px; }
  .return-address { position: absolute; left: 22px; top: 66px; font-size: 6px; color: var(--ink-soft); }

  /* envelope back */
  .envelope-back { left: 55px; top: 348px; width: 502px; height: 209px; }
  .envelope-back svg { position: absolute; left: 0; top: 0; }

  /* letterhead */
  .letterhead { left: 614px; top: 36px; width: 452px; height: 583px; }
  .letterhead .brand-lockup { left: 52px; top: 12px; }
  .letterhead .brand-name { font-size: 20px; }
  .letterhead .brand-dot { width: 14px; height: 14px; }
  .letterhead-watermark {
    position: absolute; right: 26px; bottom: 26px; width: 150px; height: 150px;
    border-radius: 50%; background: var(--faint);
  }
  .letterhead-footer { position: absolute; left: 30px; bottom: 20px; font-size: 6px; line-height: 1.5; color: var(--ink-soft); }

  /* business cards */
  .card-front { left: 953px; top: 120px; width: 225px; height: 130px; }
  .card-front .brand-lockup { left: 92px; top: 10px; gap: 1px; }
  .card-front .brand-name { font-size: 12px; }
  .card-front .brand-dot { width: 8px; height: 8px; margin-right: 3px; }
  .card-front .brand-tag { font-size: 4px; }
  .card-watermark {
    position: absolute; right: -18px; bottom: -14px; width: 90px; height: 90px;
    border-radius: 50%; background: var(--faint);
  }
  .card-person { position: absolute; left: 12px; top: 52px; font-size: 5px; line-height: 1.4; color: var(--ink); }
  .card-person .person-name { font-weight: 700; font-size: 6px; }
  .card-contact { position: absolute; left: 12px; top: 82px; font-size: 4.5px; line-height: 1.45; color: var(--ink-soft); }

  .card-back {
    left: 953px; top: 264px; width: 225px; height: 132px;
    background: radial-gradient(circle at 50% 50%, var(--brand-mid) 0%, var(--brand) 45%, var(--brand-deep) 100%);
  }
  .card-back .brand-name {
    position: absolute; left: 0; right: 0; top: 58px; text-align: center;
    font-size: 15px; color: #ffffff;
  }
</style>
</head>
<body>
<main class="showcase">
</main>

<section class="piece envelope-front" aria-label="Envelope front">
  <svg class="corner-band" width="50" height="60" viewBox="0 0 50 60" aria-hidden="true">
    <defs>
      <linearGradient id="bandEnv" x1="0" y1="0" x2="1" y2="1">
        <stop offset="0" stop-color="#0f2f56"/>
        <stop offset="0.6" stop-color="#2f6fa8"/>
        <stop offset="1" stop-color="#7fb2dc"/>
      </linearGradient>
    </defs>
    <path d="M0 0 H42 C26 8 14 22 8 60 H0 Z" fill="url(#bandEnv)"/>
  </svg>
  <div class="brand-lockup">
    <span class="brand-tag">Your roof, our care</span>
    <span class="brand-name"><span class="brand-dot"></span>BrightGable.net</span>
    <span class="brand-tag">Professional roofing you trust</span>
  </div>
  <p class="return-address">718 Quillmoor Rd., Ashvale, QX 32814</p>
</section>

<section class="piece envelope-back" aria-label="Envelope back">
  <svg width="502" height="209" viewBox="0 0 502 209" aria-hidden="true">
    <path d="M0 6 L28 38 H474 L502 6" fill="none" stroke="#9aa0a6" stroke-width="1"/>
    <circle cx="251" cy="84" r="12" fill="#2c5f92"/>
  </svg>
</section>

<section class="piece letterhead" aria-label="Letterhead">
  <svg class="corner-band" width="56" height="70" viewBox="0 0 56 70" aria-hidden="true">
    <defs>
      <linearGradient id="bandLetter" x1="0" y1="0" x2="1" y2="1">
        <stop offset="0" stop-color="#0f2f56"/>
        <stop offset="0.6" stop-color="#2f6fa8"/>
        <stop offset="1" stop-color="#7fb2dc"/>
      </linearGradient>
    </defs>
    <path d="M0 0 H48 C30 10 16 26 9 70 H0 Z" fill="url(#bandLetter)"/>
  </svg>
  <div class="brand-lockup">
    <span class="brand-tag">Your roof, our care</span>
    <span class="brand-name"><span class="brand-dot"></span>BrightGable.net</span>
    <span class="brand-tag">Professional roofing you trust</span>
  </div>
  <div class="letterhead-watermark" aria-hidden="true"></div>
  <address class="letterhead-footer">
    718 Quillmoor Rd., Ashvale, QX 32814<br>
    Phone 407-555-0143 &nbsp; Fax 407-555-0144<br>
    hpemberly@brightgable.net &nbsp;|&nbsp; www.brightgable.net
  </address>
</section>

<section class="piece card-front" aria-label="Business card front">
  <div class="brand-lockup">
    <span class="brand-tag">Your roof, our care</span>
    <span class="brand-name"><span class="brand-dot"></span>BrightGable.net</span>
    <span class="brand-tag">Professional roofing you trust</span>
  </div>
  <div class="card-watermark" aria-hidden="true"></div>
  <div class="card-person">
    <p class="person-name">Hal Pemberly</p>
    <p>President</p>
  </div>
  <address class="card-contact">
    718 Quillmoor Rd., Ashvale, QX 32814<br>
    Phone 407-555-0143 &nbsp; Fax 407-555-0144<br>
    hpemberly@brightgable.net<br>
    www.brightgable.net
  </address>
</section>

<section class="piece card-back" role="img" aria-label="Business card back: blue radial backdrop with fine dot texture">
  <span class="brand-name">BrightGable.net</span>
</section>
</body>
</html>
```